2021 Halberd Ensemble Summer Music Institute & Festival

we need a brochure for the Summer music school and series of concerts. We want it to be modern, and informative. Please look at our web page:
http://academy.halberdensemble.org/halberd-summer-music-institute/

Target Market(s)

middle-class families with school and college children

Requirements
Must have
• text from the web page:
Also
http://halberdensemble.org/category/2021-halberd-summer-music-festival/
(this will be updated soon, but the events have to be listed in the brochure
Please use graphics from the pages and the attached files.

```html
<!DOCTYPE html>
<html lang="en">
<head>
<meta charset="utf-8">
<title>2021 Halberd Ensemble Summer Music Institute &amp; Festival – Brochure Spread</title>
<link href="https://fonts.googleapis.com/css2?family=Montserrat:ital,wght@0,400;0,600;0,700;0,800;1,300;1,400;1,600;1,700;1,800&display=swap" rel="stylesheet">
<style>
:root{
  --indigo:#2b2287;
  --violet:#5f53b3;
  --paper:#f4f4f6;
  --paper-shade:#e6e6ea;
  --ink:#2b2b2e;
  --ink-soft:#55555c;
  --white:#ffffff;
  --backdrop:#3a3a3a;
}
*{box-sizing:border-box;margin:0;padding:0}
html,body{width:1200px;height:833px;overflow:hidden;background:var(--backdrop)}
body{font-family:"Montserrat",sans-serif;color:var(--ink)}
.spread{position:absolute;left:30px;top:26px;width:1140px;height:780px;display:flex;box-shadow:0 12px 40px rgba(0,0,0,.5)}
.page{position:relative;width:570px;height:780px;background:var(--paper);overflow:hidden}
.page--left{background:linear-gradient(90deg,var(--paper) 85%,var(--paper-shade))}
.page--right{background:linear-gradient(90deg,var(--paper-shade),var(--paper) 12%)}
.page-rule{position:absolute;left:0;right:0;bottom:0;height:5px;background:var(--indigo)}

/* left page */
.hero-band{position:absolute;left:0;top:0;width:570px;height:250px}
.hero-rule{position:absolute;left:46px;top:34px;width:3px;height:118px;background:var(--white)}
.hero-title{position:absolute;left:62px;top:30px;color:var(--white);font-weight:700;font-style:italic;font-size:21px;line-height:29px;letter-spacing:.2px}
.intro-box{position:absolute;left:40px;top:168px;width:500px;height:78px;background:var(--white);border-radius:14px;padding:12px 20px;font-style:italic;font-weight:600;font-size:11px;line-height:14px;color:var(--ink)}
.instrument-tab{position:absolute;left:28px;top:232px;width:520px;height:24px;background:var(--violet);clip-path:polygon(0 0,100% 0,97% 100%,0 100%);color:var(--white);font-style:italic;font-weight:600;font-size:11.5px;line-height:24px;padding-left:24px}
.body-copy{position:absolute;left:30px;top:266px;width:505px;font-style:italic;font-weight:300;font-size:8.6px;line-height:11.6px;color:var(--ink-soft)}
.body-copy p{margin-bottom:7px}
.body-copy strong{font-weight:700;color:var(--ink)}
.drop-cap{float:left;font-style:normal;font-weight:800;font-size:38px;line-height:30px;margin:2px 4px 0 0;color:var(--ink)}
.camp-notes{position:absolute;left:30px;top:508px;width:300px;list-style:none;font-style:italic;font-weight:600;font-size:8.8px;line-height:11px;color:var(--ink)}
.camp-notes li{position:relative;padding-left:14px;margin-bottom:3px}
.camp-notes svg{position:absolute;left:0;top:1px;width:9px;height:9px}
.photo{border-radius:22px}
.photo--concert{position:absolute;left:340px;top:520px;width:205px;height:230px;background:linear-gradient(160deg,#8a9a6a,#4f5a3c 55%,#2e3025)}

/* right page */
.festival-tab{position:absolute;left:58px;top:0;width:280px;height:170px}
.festival-title{position:absolute;left:86px;top:42px;color:var(--white);font-weight:800;font-size:21px;line-height:24px;letter-spacing:.4px}
.event{position:absolute;font-weight:700;color:var(--ink)}
.event-date{display:block;height:20px;background:var(--violet);clip-path:polygon(0 0,92% 0,100% 100%,0 100%);color:var(--white);font-size:13px;line-height:20px;padding-left:14px;letter-spacing:1px}
.event--dark .event-date{background:var(--indigo)}
.event-detail{display:block;font-size:13.5px;line-height:16px;padding-left:4px;margin-top:2px}
.event-day{display:block;font-size:13px;line-height:14px;padding-left:4px}
.portrait{position:absolute;left:36px;width:118px;height:78px;border:2px solid var(--indigo);border-radius:10px}
.portrait--1{top:182px;background:linear-gradient(135deg,#c89a7a,#b0302e 60%,#6e8aa0)}
.portrait--2{top:276px;background:linear-gradient(135deg,#2d2a2a,#8c6a58 60%,#e8e4e0)}
.portrait--3{top:370px;background:linear-gradient(135deg,#6b5a3e,#c8b490 50%,#3e3a32)}
.portrait--4{top:464px;background:linear-gradient(135deg,#9ab0a0,#2a2a2e 55%,#6c7a70)}
.timeline-rule{position:absolute;left:332px;width:3px;height:90px;background:var(--indigo)}
.ticket-band{position:absolute;left:40px;top:584px;width:500px;height:28px;background:var(--indigo);clip-path:polygon(1.5% 0,100% 0,98.5% 100%,0 100%);color:var(--white);font-weight:700;font-size:12.5px;line-height:28px;padding-left:22px;letter-spacing:.3px}
.opera-rule{position:absolute;left:40px;top:628px;width:3px;height:44px;background:var(--indigo)}
.opera-title{position:absolute;left:54px;top:624px;color:var(--indigo);font-weight:800;font-size:18.5px;line-height:24px}
.opera-copy{position:absolute;left:40px;top:690px;width:490px;font-size:8.8px;line-height:12px;color:var(--ink-soft)}
</style>
</head>
<body>
<main class="spread">
  <!-- Left page -->
  <section class="page page--left">
    <svg class="hero-band" viewBox="0 0 570 250" preserveAspectRatio="none" aria-hidden="true">
      <defs>
        <linearGradient id="heroGrad" x1="0" y1="0" x2="1" y2="0">
          <stop offset="0" stop-color="#2b2287"/>
          <stop offset="1" stop-color="#6a5fbb"/>
        </linearGradient>
      </defs>
      <polygon points="0,0 570,0 570,245 0,175" fill="url(#heroGrad)"/>
    </svg>
    <span class="hero-rule"></span>
    <h1 class="hero-title">Chamber Music – Individual Instruction –<br>Master-Classes – Orchestra –<br>Fun &amp; Educational Activities –<br>Public Performances – Music Theory</h1>

    <p class="intro-box">In light of the COVID-19 situation, we are limiting the 2021 HMI Institute to strings and piano instructions only. The institute is open to students and adults of all ages.</p>
    <p class="instrument-tab">Instruments: Strings: violin, viola, cello, double bass, piano</p>

    <div class="body-copy">
      <p><span class="drop-cap">W</span><strong>elcome:</strong> Since 2011, our Halberd Summer Music Institute and Festival has delighted audiences with performances of chamber music works and operas. Although we are unable to perform an opera this year, our commitment to high-standard concerts is as strong as ever. The Institute's program will include chamber music coaching, chamber orchestra, music theory classes, history of composers from guest lecturers, and many public performances. Our outstanding, internationally acclaimed, and very dedicated instructors are interacting closely with students – teaching, socializing, and sharing their performance experiences. This inspirational and indispensable relationship gives our students a great boost of self-confidence and a sense of accomplishment.</p>
      <p><strong>Venues:</strong> The Festival performances take place at St. Aldric Chapel in Eastbrook, Old Meeting House of Millbridge, and the Linden Gallery of Art in Millbridge.</p>
      <p>The program is open to students and adults of all ages who demonstrate a good command of their instrument and are able to perform in a variety of chamber music and advanced orchestral settings.</p>
      <p>In order to be considered for solo performance opportunities, a student must come with a prepared repertoire including classical or romantic sonata, bravura piece, or concerto movement prepared prior to the start of the institute. Piano accompaniment will be provided.</p>
    </div>

    <ul class="camp-notes">
      <li><svg viewBox="0 0 10 10"><circle cx="5" cy="5" r="4.2" fill="none" stroke="#5f53b3" stroke-width="1"/><path d="M3 5.2l1.4 1.3L7 3.8" fill="none" stroke="#5f53b3" stroke-width="1"/></svg>Arrival time between 9:30 to 10 am (earlier drop off may be arranged as needed)</li>
      <li><svg viewBox="0 0 10 10"><circle cx="5" cy="5" r="4.2" fill="none" stroke="#5f53b3" stroke-width="1"/><path d="M3 5.2l1.4 1.3L7 3.8" fill="none" stroke="#5f53b3" stroke-width="1"/></svg>Pick up time 2 pm.</li>
      <li><svg viewBox="0 0 10 10"><circle cx="5" cy="5" r="4.2" fill="none" stroke="#5f53b3" stroke-width="1"/><path d="M3 5.2l1.4 1.3L7 3.8" fill="none" stroke="#5f53b3" stroke-width="1"/></svg>Parents are required to provide transportation to camp and performance venues.</li>
      <li><svg viewBox="0 0 10 10"><circle cx="5" cy="5" r="4.2" fill="none" stroke="#5f53b3" stroke-width="1"/><path d="M3 5.2l1.4 1.3L7 3.8" fill="none" stroke="#5f53b3" stroke-width="1"/></svg>Please bring your own masks and hand sanitizer as needed.</li>
      <li><svg viewBox="0 0 10 10"><circle cx="5" cy="5" r="4.2" fill="none" stroke="#5f53b3" stroke-width="1"/><path d="M3 5.2l1.4 1.3L7 3.8" fill="none" stroke="#5f53b3" stroke-width="1"/></svg>We will provide additional sanitizer as needed.</li>
      <li><svg viewBox="0 0 10 10"><circle cx="5" cy="5" r="4.2" fill="none" stroke="#5f53b3" stroke-width="1"/><path d="M3 5.2l1.4 1.3L7 3.8" fill="none" stroke="#5f53b3" stroke-width="1"/></svg>Classes will be limited to a maximum of 10 students.</li>
      <li><svg viewBox="0 0 10 10"><circle cx="5" cy="5" r="4.2" fill="none" stroke="#5f53b3" stroke-width="1"/><path d="M3 5.2l1.4 1.3L7 3.8" fill="none" stroke="#5f53b3" stroke-width="1"/></svg>Please bring lunch and a snack.</li>
      <li><svg viewBox="0 0 10 10"><circle cx="5" cy="5" r="4.2" fill="none" stroke="#5f53b3" stroke-width="1"/><path d="M3 5.2l1.4 1.3L7 3.8" fill="none" stroke="#5f53b3" stroke-width="1"/></svg>Students must have black folders labeled with their names, a notebook, staff paper, and a pencil on the first day of camp.</li>
      <li><svg viewBox="0 0 10 10"><circle cx="5" cy="5" r="4.2" fill="none" stroke="#5f53b3" stroke-width="1"/><path d="M3 5.2l1.4 1.3L7 3.8" fill="none" stroke="#5f53b3" stroke-width="1"/></svg>Please bring a music stand.</li>
    </ul>

    <div class="photo photo--concert" role="img" aria-label="Photo of an outdoor evening chamber concert under trees with an audience"></div>
    <span class="page-rule"></span>
  </section>

  <!-- Right page -->
  <section class="page page--right">
    <svg class="festival-tab" viewBox="0 0 280 170" preserveAspectRatio="none" aria-hidden="true">
      <defs>
        <linearGradient id="tabGrad" x1="0" y1="0" x2="1" y2="0">
          <stop offset="0" stop-color="#2b2287"/>
          <stop offset="1" stop-color="#6a5fbb"/>
        </linearGradient>
      </defs>
      <polygon points="0,0 280,0 280,170 0,135" fill="url(#tabGrad)"/>
    </svg>
    <h2 class="festival-title">2021 HALBERD<br>SUMMER MUSIC<br>FESTIVAL</h2>

    <div class="portrait portrait--1" role="img" aria-label="Portrait photo of soprano Marina Cortez"></div>
    <div class="event" style="left:166px;top:186px;width:150px">
      <span class="event-date">07/30/21</span>
      <span class="event-detail">7:30pm<br>Marina Cortez</span>
      <span class="event-day">Tue, May 4th, 2021</span>
    </div>

    <div class="portrait portrait--2" role="img" aria-label="Portrait photo of violinist Elira Kostani"></div>
    <div class="event" style="left:166px;top:280px;width:150px">
      <span class="event-date">07/29/21</span>
      <span class="event-detail">7:30pm<br>Elira Kostani<br>Recital</span>
    </div>

    <div class="portrait portrait--3" role="img" aria-label="Photo of a string ensemble performing in a gallery hall"></div>
    <div class="event" style="left:166px;top:374px;width:150px">
      <span class="event-date">07/28/21</span>
      <span class="event-detail">7:30pm<br>Students' concert</span>
    </div>

    <div class="portrait portrait--4" role="img" aria-label="Portrait photo of violinist Tomas Varenne"></div>
    <div class="event" style="left:166px;top:452px;width:150px">
      <span class="event-day">Sunday</span>
      <span class="event-date">07/18/21</span>
      <span class="event-detail">7:30pm<br>Piano Quintets</span>
    </div>

    <span class="timeline-rule" style="top:196px"></span>
    <div class="event event--dark" style="left:346px;top:198px;width:180px">
      <span class="event-date">08/01/21</span>
      <span class="event-detail">7:30pm<br>Mendelssohn for strings 2</span>
      <span class="event-day">Tue, May 4th, 2021</span>
    </div>

    <span class="timeline-rule" style="top:300px"></span>
    <div class="event event--dark" style="left:346px;top:304px;width:180px">
      <span class="event-date">07/25/21</span>
      <span class="event-detail">7:30pm<br>Mendelssohn for<br>Strings 1</span>
    </div>

    <span class="timeline-rule" style="top:400px;height:80px"></span>
    <div class="event event--dark" style="left:346px;top:402px;width:180px">
      <span class="event-date">07/23/21</span>
      <span class="event-detail">7:30pm<br>Bach cantata TBA</span>
    </div>

    <span class="timeline-rule" style="top:488px;height:80px"></span>
    <div class="event event--dark" style="left:346px;top:490px;width:180px">
      <span class="event-date">07/22/21</span>
      <span class="event-detail">7:30pm<br>Tomas Varenne –<br>Recital</span>
    </div>

    <p class="ticket-band">purchase tickets online at www.halberdensemble.tixbooth.com</p>

    <span class="opera-rule"></span>
    <h3 class="opera-title">June/July 2021 PUCCINI – LA BOHEME<br>Riverside Lyric Opera Production</h3>
    <p class="opera-copy">RIVERSIDE LYRIC OPERA &amp; THE HALBERD ENSEMBLE – MAIN STAGE: PUCCINI – LA BOHEME July 2021 (Dates, Locations, and times TBA) Fully staged with the Riverside Lyric Opera: The production will also include young singers from the Halberd Academy in Millbridge Program Cast to be announced at a later date, Stage [...]</p>
    <span class="page-rule"></span>
  </section>
</main>
</body>
</html>
```